Business card / stationery design
Pemberton Hale Warrick
Project: Business card / stationery design
Business card / stationery design - Engineering
Creative Brief
Use specific fonts
Gill Sans MT, Calibri, Corbel, Lucida Sans UC or similar
Professional
Derek R. Pemberton, P.E., LEED A.P., CPMP
Principal
4738 E. Harrowgate Ave., Suite C-212B, Springfield, Missouri 65809
dpemberton@pembertonhalewarrick.example
www.pembertonhalewarrick.example
We would like to use only the logo from the attached file. We like the current color arrangement, but would be interested in seeing it in other colors. Also the slightly gray color behind the logo should just be white or whatever the background color is. A couple of examples are attached. The main text adjacent to the logo should read: Pemberton Hale Warrick. Secondary text will be similar to: Engineering & Energy Services.
We are interested in your ideas.

```html
<!DOCTYPE html>
<html lang="en">
<head>
<meta charset="utf-8">
<title>Pemberton Hale Warrick — Business Cards</title>
<link rel="stylesheet" href="https://fonts.googleapis.com/css2?family=Cabin:wght@400;600&family=Cormorant+Garamond:wght@500;600&display=swap">
<style>
  :root {
    --page-bg: #ececea;
    --card-white: #ffffff;
    --card-dark: #2b2b2b;
    --card-dark-edge: #1f1f1f;
    --ink: #3a3a3a;
    --ink-soft: #6a6a6a;
    --brand-green: #6cb33f;
    --brand-blue: #1f6fb5;
    --stripe-pale: #e4f1d8;
    --back-text: #e8e8e8;
  }
  * { box-sizing: border-box; margin: 0; padding: 0; }
  html, body { width: 1200px; height: 444px; overflow: hidden; }
  body {
    background: var(--page-bg);
    font-family: "Cabin", "Gill Sans", sans-serif;
    color: var(--ink);
    position: relative;
  }
  .card {
    position: absolute;
    top: 72px;
    width: 504px;
    height: 300px;
    border-radius: 12px;
    overflow: hidden;
  }
  .card--front { left: 72px; background: var(--card-white); }
  .card--back { left: 624px; background: var(--card-dark); }

  /* Front */
  .front__stripes {
    position: absolute;
    left: 0; top: 0;
    width: 62%; height: 100%;
    background: linear-gradient(100deg, var(--stripe-pale) 0%, rgba(228,241,216,0.55) 60%, rgba(255,255,255,0) 100%);
  }
  .front__square {
    position: absolute;
    left: 62px; top: 40px;
    width: 100px; height: 100px;
    background: var(--brand-green);
  }
  .front__name {
    position: absolute;
    left: 18px; top: 184px;
    font-family: "Cormorant Garamond", "Gill Sans", serif;
    font-weight: 600;
    font-size: 19px;
    letter-spacing: 0.04em;
    text-transform: uppercase;
    white-space: nowrap;
    color: var(--ink);
  }
  .person {
    position: absolute;
    right: 30px; top: 28px;
    text-align: right;
  }
  .person__name {
    font-family: "Cormorant Garamond", "Gill Sans", serif;
    font-weight: 600;
    font-size: 14px;
    letter-spacing: 0.06em;
    text-transform: uppercase;
  }
  .person__credentials, .person__title {
    font-size: 8px;
    letter-spacing: 0.08em;
    text-transform: uppercase;
    color: var(--ink-soft);
    margin-top: 2px;
  }
  .front__tab {
    position: absolute;
    right: 0; top: 158px;
    width: 7px; height: 40px;
    background: linear-gradient(var(--brand-green) 50%, var(--brand-blue) 50%);
  }
  .contact {
    font-size: 8px;
    line-height: 1.45;
    color: var(--ink-soft);
    position: absolute;
    white-space: nowrap;
  }
  .contact__address { left: 300px; top: 204px; }
  .contact__phones { right: 30px; top: 246px; text-align: right; }
  .contact__online { left: 150px; top: 266px; }
  .contact__label { color: var(--ink); font-weight: 600; }

  /* Back */
  .back__texture {
    position: absolute; inset: 0;
    background: radial-gradient(ellipse at 50% 40%, #363636 0%, var(--card-dark) 55%, var(--card-dark-edge) 100%);
  }
  .back__mark {
    position: absolute;
    left: 0; right: 0; top: 72px;
    display: flex;
    flex-direction: column;
    align-items: center;
    gap: 14px;
  }
  .back__square {
    width: 70px; height: 70px;
    background: var(--brand-green);
  }
  .back__name {
    font-family: "Cormorant Garamond", "Gill Sans", serif;
    font-weight: 600;
    font-size: 16px;
    letter-spacing: 0.08em;
    text-transform: uppercase;
    color: var(--back-text);
    white-space: nowrap;
  }
  .back__web {
    position: absolute;
    left: 0; right: 0; top: 222px;
    text-align: center;
    font-family: "Cormorant Garamond", "Gill Sans", serif;
    font-weight: 600;
    font-size: 13px;
    letter-spacing: 0.14em;
    text-transform: uppercase;
    color: var(--back-text);
  }
</style>
</head>
<body>
  <section class="card card--front" aria-label="Business card front">
    <div class="front__stripes" role="img" aria-label="Pale green diagonal stripe pattern"></div>
    <span class="front__square"></span>
    <p class="front__name">Pemberton Hale Warrick</p>
    <div class="person">
      <p class="person__name">Derek R. Pemberton</p>
      <p class="person__credentials">P.E., LEED A.P., CPMP</p>
      <p class="person__title">Principal</p>
    </div>
    <div class="front__tab"></div>
    <p class="contact contact__address">4738 E. Harrowgate Ave.,<br>Suite C-212B, Springfield,<br>Missouri 65809</p>
    <div class="contact contact__phones">
      <p><span class="contact__label">P :</span> 417.555.0142</p>
      <p><span class="contact__label">C :</span> 417.555.0187</p>
    </div>
    <div class="contact contact__online">
      <p><span class="contact__label">E :</span> dpemberton@pembertonhalewarrick.example</p>
      <p><span class="contact__label">W :</span> www.pembertonhalewarrick.example</p>
    </div>
  </section>

  <section class="card card--back" aria-label="Business card back">
    <div class="back__texture" role="img" aria-label="Dark charcoal carbon-weave texture"></div>
    <div class="back__mark">
      <span class="back__square"></span>
      <span class="back__name">Pemberton Hale Warrick</span>
    </div>
    <p class="back__web">www.pembertonhalewarrick.example</p>
  </section>
</body>
</html>
```